Derek Hollins Business card

Hey there, I’m hoping to have a business card designed. I’m in Real estate and just switched to a new Brokerage called: The Property Quarter

The back could just be the company name maybe or whatever looks good!

I’ve attached some logos of our company and some cards my buddy had done up.

On the card:
Derek Hollins
derekhollins@mailbox-demo.com
587-214-6093
derekhollins-demo.ca

Target Market(s)

Home buyers and sellers

Industry/Entity Type

Real Estate

Contact Information for Business Card

just looking for a cool and modern design with my picture on it. I like the idea of Black and red being used.

Requirements
Must have
• all the details provided. I'm open to anything. Just want a professional looking card.

```html
<!DOCTYPE html>
<html lang="en">
<head>
<meta charset="utf-8">
<title>Derek Hollins – Business Card</title>
<link href="https://fonts.googleapis.com/css2?family=Poppins:wght@300;400;600;700;800&display=swap" rel="stylesheet">
<style>
  :root {
    --bg: #222222;
    --card: #25242a;
    --red: #d21f3c;
    --edge: #e0122e;
    --white: #ffffff;
    --muted: #e8e8ea;
  }
  * { box-sizing: border-box; margin: 0; padding: 0; }
  html, body {
    width: 1200px; height: 711px; overflow: hidden;
    background: var(--bg);
    font-family: "Poppins", sans-serif;
  }
  .stage {
    width: 1200px; height: 711px;
    display: flex; align-items: center; justify-content: center; gap: 40px;
  }
  .card {
    position: relative;
    width: 540px; height: 309px;
    background: var(--card);
    border-radius: 22px;
    border-bottom: 3px solid var(--edge);
    overflow: hidden;
  }
  /* Front */
  .card-front { display: flex; align-items: center; justify-content: center; }
  .brand-name {
    color: var(--white);
    font-weight: 800;
    text-transform: uppercase;
    letter-spacing: 1px;
    line-height: 1;
  }
  .card-front .brand-name { font-size: 40px; text-align: center; }
  .card-front .brand-name span { display: block; }

  /* Back */
  .card-back .brand-name {
    position: absolute; left: 26px; top: 30px;
    font-size: 20px;
  }
  .portrait {
    position: absolute; right: 0; bottom: 0;
    width: 250px; height: 275px;
    background: radial-gradient(ellipse at 55% 30%, #c99a84 0%, #8a6657 22%, #2b2a31 50%, #1d1c22 100%);
    border-top-left-radius: 120px;
  }
  .name {
    position: absolute; left: 0; top: 170px;
    display: flex; align-items: center; gap: 10px;
    font-size: 27px; line-height: 1;
  }
  .name-bar { width: 16px; height: 34px; background: var(--red); }
  .name-first { color: var(--red); font-weight: 700; }
  .name-last { color: var(--white); font-weight: 300; }
  .contacts {
    position: absolute; left: 40px; top: 222px;
    list-style: none;
    font-size: 12.5px; color: var(--muted); font-weight: 400;
  }
  .contacts li { display: flex; align-items: center; gap: 9px; line-height: 22px; }
  .contacts svg { width: 13px; height: 13px; fill: var(--red); flex: none; }
</style>
</head>
<body>
<main class="stage">
  <section class="card card-front" aria-label="Card front">
    <p class="brand-name"><span>The Property</span><span>Quarter</span></p>
  </section>

  <section class="card card-back" aria-label="Card back">
    <p class="brand-name">The Property Quarter</p>
    <div class="portrait" role="img" aria-label="Portrait photo of Derek Hollins in a dark blazer and white shirt"></div>
    <h1 class="name">
      <span class="name-bar"></span>
      <span class="name-first">Derek</span>
      <span class="name-last">Hollins</span>
    </h1>
    <ul class="contacts">
      <li>
        <svg viewBox="0 0 24 24" aria-hidden="true"><path d="M6.6 10.8a15.1 15.1 0 0 0 6.6 6.6l2.2-2.2c.3-.3.7-.4 1-.2 1.1.4 2.3.6 3.6.6.6 0 1 .4 1 1V20c0 .6-.4 1-1 1C10.6 21 3 13.4 3 4c0-.6.4-1 1-1h3.5c.6 0 1 .4 1 1 0 1.3.2 2.5.6 3.6.1.3 0 .7-.2 1z"/></svg>
        587-214-6093
      </li>
      <li>
        <svg viewBox="0 0 24 24" aria-hidden="true"><path d="M12 2a10 10 0 1 0 0 20 10 10 0 0 0 0-20zm6.9 6h-3a15.7 15.7 0 0 0-1.4-3.6A8 8 0 0 1 18.9 8zM12 4c.8 1.2 1.5 2.5 1.9 4h-3.8c.4-1.5 1.1-2.8 1.9-4zM4.3 14a8.2 8.2 0 0 1 0-4h3.4a16 16 0 0 0 0 4zm.8 2h3a15.7 15.7 0 0 0 1.4 3.6A8 8 0 0 1 5.1 16zm3-8h-3a8 8 0 0 1 4.4-3.6C8.9 5.5 8.4 6.7 8.1 8zM12 20c-.8-1.2-1.5-2.5-1.9-4h3.8c-.4 1.5-1.1 2.8-1.9 4zm2.3-6H9.7a14.7 14.7 0 0 1 0-4h4.6a14.7 14.7 0 0 1 0 4zm.3 5.6c.6-1.1 1.1-2.3 1.4-3.6h3a8 8 0 0 1-4.4 3.6zm1.7-5.6a16 16 0 0 0 0-4h3.4a8.2 8.2 0 0 1 0 4z"/></svg>
        www.derekhollins-demo.ca
      </li>
      <li>
        <svg viewBox="0 0 24 24" aria-hidden="true"><path d="M3 5h18c.6 0 1 .4 1 1v12c0 .6-.4 1-1 1H3c-.6 0-1-.4-1-1V6c0-.6.4-1 1-1zm9 7.4L4.4 7H4v.8l8 5.7 8-5.7V7h-.4z"/></svg>
        derekhollins@mailbox-demo.com
      </li>
    </ul>
  </section>
</main>
</body>
</html>
```